Residential home builder needs a fresh looking business card

We require a fresh looking business card for our business. We like the clean modern look. I have uploaded out logo and our email footer that incorporates some different elements. Blacks and Whites are good but i will leave this up to the design crowd creative minds.

our slogan is:
your idea of the perfect home

website (temporary site) but similar look and feel to the finished one
bluegumdwellings.com.au

We also have intentions to apply the same look and feel to the rest of our stationary (letterheads, envelopes, site signs, vehicles etc)

Home Builder

```html
<!DOCTYPE html>
<html lang="en">
<head>
<meta charset="utf-8">
<title>Bluegum Dwellings – Business Card</title>
<link rel="stylesheet" href="https://fonts.googleapis.com/css2?family=Barlow:wght@400;500;600&family=Montserrat:wght@300;400&display=swap">
<style>
  :root {
    --backdrop: #e9e6e2;
    --card-white: #f7f7f7;
    --ink: #1f1f1f;
    --charcoal: #2b2b2b;
    --charcoal-light: #333333;
    --slogan-band: #3b3b3b;
    --accent: #f2cf1f;
    --muted: #3c3c3c;
  }
  * { box-sizing: border-box; margin: 0; padding: 0; }
  html, body {
    width: 1200px; height: 900px; overflow: hidden;
    background: var(--backdrop);
  }
  .canvas { position: relative; width: 1200px; height: 900px; }

  .card {
    position: absolute; left: 354px; width: 488px; height: 271px;
    box-shadow: 0 2px 6px rgba(0,0,0,0.25);
  }

  /* Front */
  .card-front {
    top: 157px; background: var(--card-white);
    font-family: "Barlow", Arial, sans-serif; color: var(--ink);
  }
  .edge-strip { position: absolute; left: 0; top: 0; width: 17px; height: 100%; background: var(--charcoal); }
  .edge-accent { position: absolute; left: 0; top: 61px; width: 17px; height: 33px; background: var(--accent); }
  .holder-name { position: absolute; left: 33px; top: 59px; font-size: 21px; font-weight: 400; letter-spacing: 0.2px; }
  .holder-reg { position: absolute; left: 33px; top: 84px; font-size: 12px; color: var(--muted); }

  .brand { position: absolute; left: 282px; top: 92px; width: 180px; display: flex; align-items: center; gap: 8px; }
  .brand-square { width: 16px; height: 16px; background: var(--accent); flex: none; }
  .brand-name { font-size: 22px; font-weight: 500; color: var(--ink); white-space: nowrap; }

  .contact { position: absolute; left: 33px; font-size: 12.5px; line-height: 17px; color: var(--ink); }
  .contact-direct { top: 162px; }
  .contact-office { top: 203px; }
  .label { color: var(--accent); margin-right: 4px; }
  .sep { margin-left: 6px; }
  .web { font-weight: 600; }

  /* Back */
  .card-back { top: 467px; background: var(--charcoal); overflow: hidden; }
  .emboss-area {
    position: absolute; inset: 0;
    background: linear-gradient(135deg, var(--charcoal-light), var(--charcoal));
  }
  .slogan {
    position: absolute; left: 16px; top: 130px; height: 24px; padding: 0 6px;
    background: var(--slogan-band); color: var(--accent);
    font-family: "Montserrat", Arial, sans-serif; font-weight: 300; font-size: 15.5px;
    line-height: 24px; letter-spacing: 0.3px; white-space: nowrap;
  }
</style>
</head>
<body>
<main class="canvas">
  <section class="card card-front">
    <div class="edge-strip"></div>
    <div class="edge-accent"></div>
    <h1 class="holder-name">Marcus Ellery</h1>
    <p class="holder-reg">Builders Reg: 20718</p>

    <div class="brand">
      <span class="brand-square"></span>
      <span class="brand-name">Bluegum Dwellings</span>
    </div>

    <p class="contact contact-direct">
      <span class="label">M</span>0412 555 019<br>
      <span class="label">E</span>marcus@bluegumdwellings.com.au
    </p>
    <p class="contact contact-office">
      <span class="label">P</span>08 5550 1427 <span class="label sep">F</span>08 5550 1488<br>
      PO Box 482, Harbour Vale DC, WA 6099<br>
      <span class="web">www.bluegumdwellings.com.au</span>
    </p>
  </section>

  <section class="card card-back">
    <div class="emboss-area" role="img" aria-label="Blind-embossed line drawing of house rooftops and street grid"></div>
    <p class="slogan">Your idea of the perfect home</p>
  </section>
</main>
</body>
</html>
```